Construction Directory Website Flyer

We need a postcard size +/- or somewhere around that size (something standard) flyer designed for our construction directory website. Leave a spot for tagline. Call to action is 'register your company now'. I am thinking many mini pictures of different construction to show that it is for the entire construction industry. Logo and screenshot of the homepage of the website is attached. Use same theme as webpage.

Target Market(s)

Construction Industry

Industry/Entity Type

Construction

Font styles to use
Sans Serif

Requirements
Must have
• Call to action
• Colors to match logo
• Area to add description and details.
Nice to have
• Construction Images
Should not have
• No Cartoonish types of things

```html
<!DOCTYPE html>
<html lang="en">
<head>
<meta charset="utf-8">
<title>Sitework Hub – Directory Flyer</title>
<link rel="stylesheet" href="https://fonts.googleapis.com/css2?family=Bebas+Neue&family=Lato:wght@400;700;900&display=swap">
<style>
  :root {
    --red: #d9261c;
    --orange: #f07d1e;
    --ink: #1b1b1b;
    --charcoal: #262626;
    --black: #101010;
    --paper: #ffffff;
    --mist: #e4e4e4;
    --text: #2a2a2a;
    --page: #3a3a3a;
  }
  * { margin: 0; padding: 0; box-sizing: border-box; }
  html, body { width: 1200px; height: 902px; overflow: hidden; background: var(--page); }
  .flyer {
    position: absolute; left: 83px; top: 99px;
    width: 1034px; height: 704px;
    font-family: "Lato", sans-serif;
    box-shadow: 0 10px 30px rgba(0,0,0,.5);
    overflow: hidden;
  }
  .flyer-art { position: absolute; inset: 0; }
  .brand {
    position: absolute; left: 150px; top: 60px; width: 320px; height: 50px;
    display: flex; align-items: center; gap: 14px;
  }
  .brand-mark { width: 34px; height: 34px; background: var(--red); flex: none; }
  .brand-name { font-family: "Lato", sans-serif; font-weight: 700; font-size: 34px; color: #3d3d3d; white-space: nowrap; }
  .headline {
    position: absolute; left: 490px; width: 544px; text-align: center;
    font-family: "Bebas Neue", sans-serif; color: var(--paper); white-space: nowrap; line-height: 1;
  }
  .headline-top { top: 40px; font-size: 86px; }
  .headline-sub { top: 130px; font-size: 66px; }
  .description {
    position: absolute; left: 460px; top: 226px; width: 546px; height: 220px;
    font-size: 20px; line-height: 27.5px; color: var(--text);
    text-align: justify; hyphens: manual;
  }
  .description .slant {
    float: left; width: 34px; height: 220px;
    shape-outside: polygon(0 0, 100% 0, 0 100%);
  }
  .cta {
    position: absolute; left: 448px; top: 468px; width: 560px;
    font-weight: 900; font-size: 31px; color: var(--ink); white-space: nowrap; text-align: right;
  }
  .cta .accent { color: var(--red); }
  .phone {
    position: absolute; left: 480px; top: 533px; width: 500px; height: 56px;
    display: flex; align-items: center; justify-content: center; gap: 14px;
    font-weight: 900; font-size: 40px; color: var(--paper); letter-spacing: 1px;
  }
  .web {
    position: absolute; left: 498px; top: 618px;
    display: flex; align-items: center; gap: 14px;
    font-size: 20px; color: var(--paper); letter-spacing: 3.4px;
  }
</style>
</head>
<body>
<main class="flyer">
  <svg class="flyer-art" width="1034" height="704" viewBox="0 0 1034 704" aria-hidden="false">
    <defs>
      <linearGradient id="band" x1="0" x2="1">
        <stop offset="0" stop-color="#d9261c"/>
        <stop offset=".45" stop-color="#f07d1e"/>
        <stop offset="1" stop-color="#d9261c"/>
      </linearGradient>
      <linearGradient id="body" x1="0" y1="0" x2="0" y2="1">
        <stop offset="0" stop-color="#1c1c1c"/>
        <stop offset="1" stop-color="#2e2e2e"/>
      </linearGradient>
      <linearGradient id="panel" x1="0" x2="1">
        <stop offset="0" stop-color="#ffffff"/>
        <stop offset="1" stop-color="#e2e2e2"/>
      </linearGradient>
      <linearGradient id="button" x1="0" y1="0" x2="0" y2="1">
        <stop offset="0" stop-color="#f38a24"/>
        <stop offset="1" stop-color="#dc3a1c"/>
      </linearGradient>
      <linearGradient id="sky1" x1="0" y1="0" x2="0" y2="1">
        <stop offset="0" stop-color="#3d7cc4"/><stop offset=".6" stop-color="#a9c3d8"/><stop offset="1" stop-color="#b08a5c"/>
      </linearGradient>
      <linearGradient id="sky2" x1="0" y1="0" x2="0" y2="1">
        <stop offset="0" stop-color="#7fb0dc"/><stop offset=".45" stop-color="#5d7d3e"/><stop offset="1" stop-color="#4a4a48"/>
      </linearGradient>
      <linearGradient id="sky3" x1="0" y1="0" x2="0" y2="1">
        <stop offset="0" stop-color="#cfdceb"/><stop offset=".6" stop-color="#8b8f96"/><stop offset="1" stop-color="#a58f74"/>
      </linearGradient>
    </defs>

    <rect class="body-bg" x="0" y="0" width="1034" height="704" fill="url(#body)"/>
    <rect class="left-shade" x="0" y="28" width="100" height="186" fill="var(--black)"/>
    <rect class="left-accent" x="0" y="214" width="88" height="320" fill="var(--red)"/>

    <polygon class="copy-panel" points="472,214 1034,214 1034,534 422,534" fill="url(#panel)"/>

    <polygon class="logo-stripe" points="110,28 126,28 104,140 88,140" fill="var(--orange)"/>
    <polygon class="logo-panel" points="126,28 498,28 476,140 104,140" fill="var(--paper)"/>
    <polygon class="logo-stripe" points="498,28 514,28 492,140 476,140" fill="var(--red)"/>

    <g role="img" aria-label="Photo: site engineer in hard hat and safety vest reviewing plans beside a tower crane over a city">
      <polygon points="102,144 480,144 470,296 80,296" fill="url(#sky1)" stroke="#fff" stroke-width="4"/>
    </g>
    <g role="img" aria-label="Photo: road roller compacting fresh asphalt on a highway">
      <polygon points="67,317 447,317 437,486 42,486" fill="url(#sky2)" stroke="#fff" stroke-width="4"/>
    </g>
    <g role="img" aria-label="Photo: foreman in blue hard hat checking a tablet on a building site">
      <polygon points="32,509 404,509 380,676 2,676" fill="url(#sky3)" stroke="#fff" stroke-width="4"/>
    </g>

    <polygon class="cta-button" points="452,526 1002,526 977,594 472,594" fill="url(#button)"/>

    <rect class="band-top" x="0" y="0" width="1034" height="28" fill="url(#band)"/>
    <rect class="band-bottom" x="0" y="676" width="1034" height="28" fill="url(#band)"/>
  </svg>

  <div class="brand">
    <span class="brand-mark"></span>
    <span class="brand-name">Sitework Hub</span>
  </div>

  <h1 class="headline headline-top">LOREM IPSUM IS</h1>
  <h2 class="headline headline-sub">SIMPLY DUMMY TEXT</h2>

  <p class="description"><span class="slant"></span>Lorem Ipsum is simply dummy text of the printing and typesetting industry. Lorem Ipsum has been the industry's standard dummy text ever since the 1500s, when an unknown printer took a galley of type and scrambled it to make a type specimen bookt has survived not only five centuries, but also the leap into electronic typesetting, remaining essen&shy;tially unchanged.</p>

  <p class="cta">REGISTER YOUR <span class="accent">COMPANY NOW</span></p>

  <p class="phone">
    <svg width="36" height="36" viewBox="0 0 36 36" aria-hidden="true">
      <circle cx="18" cy="18" r="15.5" fill="none" stroke="#1b1b1b" stroke-width="3"/>
      <path d="M12.5 10.5c1-.8 2-.6 2.6.3l1.6 2.6c.5.8.3 1.6-.4 2.2l-1 .8c.9 2 2.4 3.6 4.4 4.6l.8-1c.6-.7 1.5-.9 2.3-.4l2.6 1.6c.9.6 1 1.7.3 2.6l-1.2 1.4c-.8.9-2 1.1-3.2.6-4.4-1.8-7.7-5.2-9.5-9.6-.4-1.2-.2-2.4.7-3.1z" fill="#1b1b1b"/>
    </svg>
    <span class="phone-number">000-123-4567-890</span>
  </p>

  <p class="web">
    <svg width="22" height="22" viewBox="0 0 22 22" aria-hidden="true">
      <g fill="none" stroke="#f07d1e" stroke-width="2">
        <circle cx="11" cy="11" r="9"/>
        <ellipse cx="11" cy="11" rx="4" ry="9"/>
        <path d="M2 11h18M4 6h14M4 16h14"/>
      </g>
    </svg>
    <span class="web-address">www.websiteaddress.com</span>
  </p>
</main>
</body>
</html>
```